Quillfern Nightclub Flyer (Updated)

Flyer for facebook, square is fine, or rectangular. Here is the text:
QUILLFERN
Nightclub + Lounge
presents

SPLIT DECK WEDNESDAY
Nov 29 2018

CLUB FLOOR:
GORDY B2B RALPH
THEODORE BRUSKVIK

LOUNGE:
OTIS B2B HALF TIDE
COPPER FENWICK

Powered by HALVERN Acoustics
4716 Larchmere Avenue 21+ 9pm-2am
quillfernvenue-example.com for VIP booth inquiries

Target Market(s)

Nightclub

Industry/Entity Type

Night Club

Font styles to use
Sans Serif

Colors

Designer to choose colors to be used in the design.

Requirements
Must have
• All the text listed, and plz keep the theme of the attached files. We want to stay consistent with the Quillfern brand
Nice to have
• Try to stay with the theme from the attachments
Should not have
• Dont' stray to far from the general theme we have from the attachments

```html
<!DOCTYPE html>
<html lang="en">
<head>
<meta charset="utf-8">
<title>Quillfern Nightclub + Lounge — Split Deck Wednesday</title>
<link rel="stylesheet" href="https://fonts.googleapis.com/css2?family=Tinos&display=swap">
<style>
  :root {
    --frame-gold: #b8b37a;
    --navy: #0c0b3f;
    --gold-text: #d6cf86;
    --cream: #f1edc4;
    --white: #ffffff;
    --emblem-gold: #76714f;
    --badge-gold: #d4cf8a;
  }
  html, body {
    margin: 0;
    padding: 0;
    width: 1200px;
    height: 1200px;
    overflow: hidden;
    background: var(--frame-gold);
  }
  .flyer {
    position: relative;
    width: 1200px;
    height: 1200px;
    background: var(--frame-gold);
    font-family: "Tinos", "Times New Roman", serif;
    color: var(--white);
  }
  .panel {
    position: absolute;
    left: 38px;
    top: 35px;
    width: 1127px;
    height: 1125px;
    background: var(--navy);
    overflow: hidden;
  }
  .backdrop-emblem {
    position: absolute;
    left: 0;
    top: 0;
  }
  .abs { position: absolute; white-space: nowrap; line-height: 1; }

  .brand-dot {
    position: absolute;
    left: 163px;
    top: 101px;
    width: 136px;
    height: 136px;
    border-radius: 50%;
    background: var(--badge-gold);
  }
  .brand-name {
    left: 31px; width: 400px; text-align: center;
    top: 278px; font-size: 52px; color: var(--cream);
  }
  .brand-sub {
    left: 31px; width: 400px; text-align: center;
    top: 351px; font-size: 29px;
  }
  .brand-presents {
    left: 31px; width: 400px; text-align: center;
    top: 381px; font-size: 42px;
  }

  .date-box {
    position: absolute;
    left: 152px; top: 491px;
    width: 160px; height: 66px;
    border: 1px solid rgba(214,207,134,0.35);
    border-bottom: none;
    text-align: center;
  }
  .date-day { display: block; margin-top: 9px; font-size: 30px; color: var(--gold-text); line-height: 1; }
  .date-year { display: block; font-size: 21px; letter-spacing: 7px; color: var(--gold-text); line-height: 1; margin-left: 7px; }
  .date-rule {
    position: absolute;
    left: 162px; top: 555px;
    width: 500px; height: 3px;
    background: linear-gradient(90deg, rgba(214,207,134,0.2), var(--gold-text) 35%, var(--gold-text) 75%, rgba(214,207,134,0.1));
  }
  .event-title { left: 366px; top: 528px; font-size: 29px; }

  .room-label { font-size: 26px; color: var(--gold-text); }
  .room-colon { font-size: 26px; color: var(--gold-text); }
  .room-acts { font-size: 26px; line-height: 27px; }

  .club-label { left: 368px; top: 602px; }
  .club-colon { left: 578px; top: 604px; }
  .club-acts { left: 604px; top: 606px; }
  .lounge-label { left: 368px; top: 721px; }
  .lounge-colon { left: 578px; top: 723px; }
  .lounge-acts { left: 604px; top: 725px; }

  .venue-info {
    position: absolute;
    left: 150px; width: 880px;
    top: 841px;
    text-align: center;
    font-size: 26px;
    line-height: 27px;
    letter-spacing: 6px;
  }

  .vip-bar {
    position: absolute;
    left: 174px; top: 951px;
    width: 814px; height: 54px;
    border: 1px solid rgba(214,207,134,0.3);
    border-bottom: none;
    text-align: center;
    font-size: 22px;
    letter-spacing: 2px;
    line-height: 54px;
    white-space: nowrap;
  }
  .vip-url { color: var(--gold-text); }
  .vip-rule {
    position: absolute;
    left: 190px; top: 1003px;
    width: 790px; height: 3px;
    background: linear-gradient(90deg, rgba(214,207,134,0.15), var(--gold-text) 30%, var(--gold-text) 70%, rgba(214,207,134,0.15));
  }
  .top-rule {
    position: absolute;
    left: 190px; top: 951px;
    width: 790px; height: 2px;
    background: linear-gradient(90deg, rgba(214,207,134,0.1), rgba(214,207,134,0.8) 50%, rgba(214,207,134,0.1));
  }
</style>
</head>
<body>
<div class="flyer">
  <div class="panel">
    <svg class="backdrop-emblem" width="1127" height="1125" viewBox="0 0 1127 1125" aria-hidden="true">
      <defs>
        <radialGradient id="emblemTone" cx="0.45" cy="0.45" r="0.6">
          <stop offset="0" stop-color="#87825c"/>
          <stop offset="1" stop-color="#6a6548"/>
        </radialGradient>
      </defs>
      <circle cx="1026" cy="301" r="318" fill="url(#emblemTone)"/>
    </svg>

    <div class="brand-dot" aria-hidden="true"></div>
    <div class="abs brand-name">QUILLFERN</div>
    <div class="abs brand-sub">Nightclub + Lounge</div>
    <div class="abs brand-presents">presents</div>

    <div class="date-box">
      <span class="date-day">NOV 29</span>
      <span class="date-year">2018</span>
    </div>
    <div class="date-rule"></div>
    <div class="abs event-title">SPLIT DECK WEDNESDAY</div>

    <div class="abs room-label club-label">CLUB FLOOR</div>
    <div class="abs room-colon club-colon">:</div>
    <div class="abs room-acts club-acts">GORDY B2B RALPH<br>THEODORE BRUSKVIK.</div>

    <div class="abs room-label lounge-label">LOUNGE</div>
    <div class="abs room-colon lounge-colon">:</div>
    <div class="abs room-acts lounge-acts">OTIS B2B HALF TIDE<br>COPPER FENWICK.</div>

    <div class="venue-info">POWERED BY HALVERN ACOUSTICS<br>4716 LARCHMERE AVENUE 21+ 9PM-2AM</div>

    <div class="top-rule"></div>
    <div class="vip-bar"><span class="vip-url">QUILLFERNVENUE-EXAMPLE.COM</span> FOR VIP BOOTH INQUIRIES</div>
    <div class="vip-rule"></div>
  </div>
</div>
</body>
</html>
```